Yard Sign Design Needed

Yard sign needed for mowing & landscaping company. Would like to use the top logo with black background which is attached. Would like MOWING to be in large standout letters. The word "landscaping" can be smaller and more artistic or omitted. Will need room for phone number once design is approved. The phone number will need to stand out and look identical/similar to the word 'MOWING"

```html
<!DOCTYPE html>
<html lang="en">
<head>
<meta charset="utf-8">
<title>Brantley Contractors – Mowing Yard Sign</title>
<link rel="stylesheet" href="https://fonts.googleapis.com/css2?family=Michroma&family=Oswald:wght@600;700&family=Kaushan+Script&family=Archivo:wght@600&display=swap">
<style>
  :root {
    --page: #e9ece6;
    --sign-dark: #0b0d09;
    --grass-deep: #1c2a12;
    --lime: #9cc21f;
    --lime-bright: #b4e03a;
    --band: #8fab0a;
    --white: #ffffff;
    --ink: #050505;
  }
  * { margin: 0; padding: 0; box-sizing: border-box; }
  html, body {
    width: 1200px; height: 1200px; overflow: hidden;
    background: var(--page);
  }
  .yard-sign {
    position: absolute; left: 170px; top: 50px;
    width: 860px; height: 1100px;
    background: var(--sign-dark);
    overflow: hidden;
  }
  .mower-photo {
    position: absolute; inset: 0;
    background:
      radial-gradient(ellipse at 40% 65%, rgba(70,40,30,.45), transparent 45%),
      linear-gradient(180deg, #060706 0%, #0c0f09 28%, var(--grass-deep) 55%, #101a0a 100%);
  }
  .brand {
    position: absolute; top: 110px; left: 0; right: 0;
    display: flex; flex-direction: column; align-items: center;
  }
  .brand-square {
    width: 110px; height: 110px;
    background: var(--lime);
    margin-bottom: 44px;
  }
  .brand-name {
    font-family: "Michroma", sans-serif;
    color: var(--lime);
    text-align: center;
    line-height: 1.25;
  }
  .brand-name .primary { display: block; font-size: 56px; letter-spacing: 4px; }
  .brand-name .secondary { display: block; font-size: 34px; letter-spacing: 3px; }
  .brand-name .suffix { display: block; font-size: 20px; letter-spacing: 6px; }
  .service-script {
    position: absolute; top: 500px; left: 0; right: 0;
    text-align: center;
    font-family: "Kaushan Script", cursive;
    font-size: 66px;
    color: var(--lime-bright);
  }
  .service-frame {
    position: absolute; left: 110px; right: 50px; top: 620px; height: 260px;
    border: 4px solid var(--lime);
  }
  .service-title {
    position: absolute; top: 640px; left: 0; right: 0;
    text-align: center;
    font-family: "Oswald", sans-serif; font-weight: 700;
    font-size: 150px; line-height: 1; letter-spacing: 8px;
    color: var(--white);
  }
  .contact-band {
    position: absolute; left: 75px; right: 50px; top: 810px; height: 250px;
    background: var(--band);
    display: flex; flex-direction: column; align-items: center;
    padding-top: 18px;
  }
  .contact-label {
    font-family: "Archivo", sans-serif; font-weight: 600;
    font-size: 44px; letter-spacing: -1px; color: var(--ink);
  }
  .contact-phone {
    font-family: "Oswald", sans-serif; font-weight: 700;
    font-size: 140px; line-height: 1.05; color: var(--ink);
  }
</style>
</head>
<body>
  <div class="yard-sign">
    <div class="mower-photo" role="img" aria-label="Darkened photo of a lawn mower on freshly cut grass"></div>

    <div class="brand">
      <div class="brand-square"></div>
      <div class="brand-name">
        <span class="primary">BRANTLEY</span>
        <span class="secondary">CONTRACTORS</span>
        <span class="suffix">LLC</span>
      </div>
    </div>

    <div class="service-script">Landscaping</div>

    <div class="service-frame"></div>
    <div class="contact-band">
      <div style="height:96px"></div>
      <div class="contact-label">CONTACT US</div>
      <div class="contact-phone">555.010.0172</div>
    </div>
    <div class="service-title">MOWING</div>
  </div>
</body>
</html>
```